Diabetes control iOS/Android app design

I need a modern app design with light colors that are easy on the eyes, This app is for diabetes control. Focusing on Sweet/carb control and its daily intake .. I have uploaded some wireframe pages to design . Light colors are preferred for design. I donot need too much Hussle and data on main page.
Name/title: Glypath- Diabetes restore

Target Market(s)

Diabetes patients

Industry/Entity Type

health

Colors
0094D4
00A9DD
6FCCEA
C7EBF8
E9F6FB
00AB8E
00BBA5
67D7C9
C6EFE9
E9F9F6
59FF00
82FF00
B8FF75
E3FFCB
F4FFEA
FFC000
F8CF3A
FAE287
FDF2CF
FEFAEE

Requirements
Should not have
• complicated design. It should be simple , modern and easy o eye.

```html
<!DOCTYPE html>
<html lang="en">
<head>
<meta charset="utf-8">
<title>Glypath – Diabetes restore app screens</title>
<link href="https://fonts.googleapis.com/css2?family=Outfit:wght@400;500;600;700;800&display=swap" rel="stylesheet">
<style>
  :root{
    --board:#121212;
    --brand-blue:#228bc8;
    --brand-teal:#20b29b;
    --chart-blue:#29a8e0;
    --white:#ffffff;
    --ink:#1c1c1c;
    --muted:#6b6b6b;
    --field-line:#8a8a8a;
    --legend-bg:#f4f4f4;
    --bar-lime:#c5cb3c;
    --bar-aqua:#5bb5c0;
    --bar-navy:#2a5f78;
    --bar-coral:#ec5e6a;
    --bar-amber:#fbb630;
    --bar-violet:#8d78b2;
    --bar-jade:#3aada0;
  }
  *{box-sizing:border-box;margin:0;padding:0}
  html,body{width:728px;height:1200px;overflow:hidden}
  body{background:var(--board);font-family:'Outfit',sans-serif;position:relative}
  .sprite{position:absolute;width:0;height:0}

  .screen{position:absolute;background:var(--white);overflow:hidden;display:flex;flex-direction:column}
  .screen--phone{left:98px;top:70px;width:209px;height:451px;border-radius:26px}
  .screen--home{left:386px;top:53px;width:268px;height:476px}
  .screen--feed{left:88px;top:570px;width:268px;height:476px}
  .screen--rehab{left:390px;top:572px;width:268px;height:561px}

  .app-bar{background:var(--brand-blue);color:var(--white);display:flex;align-items:center;height:38px;padding:0 14px 0 13px;flex:none}
  .screen--phone .app-bar{height:54px;padding:16px 6px 0 7px}
  .app-bar .icon{width:16px;height:16px;color:var(--white)}
  .screen--phone .app-bar .icon{width:13px;height:13px}
  .brand{margin-left:10px;line-height:1}
  .brand-name{font-weight:700;font-size:13px;letter-spacing:.1px}
  .brand-sub{font-weight:400;font-size:8.5px;margin-top:1px}
  .screen--phone .brand{margin-left:7px}
  .screen--phone .brand-name{font-size:10.5px}
  .screen--phone .brand-sub{font-size:7px}
  .app-bar-actions{margin-left:auto;display:flex;gap:10px}
  .screen--phone .app-bar-actions{gap:8px}

  .gauge{flex:1;display:block;width:100%}

  .tab-bar{background:var(--brand-teal);height:38px;flex:none;display:flex;align-items:center;justify-content:space-around;padding:0 10px}
  .tab-bar .icon{width:17px;height:17px;color:var(--white)}
  .screen--phone .tab-bar{height:32px}
  .screen--phone .tab-bar .icon{width:14px;height:14px}
  .system-bar{background:var(--brand-blue);height:31px;flex:none;display:flex;align-items:center;justify-content:space-around;padding:0 30px}
  .system-bar .icon{width:13px;height:13px;color:var(--white)}

  .section-title{background:var(--brand-teal);color:var(--white);height:38px;flex:none;display:flex;align-items:center;justify-content:center;font-weight:700;font-size:13.5px;letter-spacing:.2px}

  .feed-form{flex:1;padding:13px 14px 0 15px}
  .field-label{display:block;font-size:10.5px;color:var(--ink);margin:5px 0 8px}
  .field-input{display:block;width:240px;height:60px;border:1px solid var(--field-line);margin-bottom:12px}
  .submit{display:flex;align-items:center;justify-content:center;width:238px;height:38px;margin-top:5px;background:var(--brand-blue);color:var(--white);font-weight:700;font-size:13px;letter-spacing:.2px}

  .rehab-body{flex:1;display:flex;flex-direction:column}
  .chart{display:block;width:268px}
  .chart-caption{text-align:center;font-size:11.5px;color:var(--ink);font-weight:500}
  .chart-caption--sugar{margin:2px 0 14px}
  .chart-caption--walk{margin:6px 0 10px}
  .legend{background:var(--legend-bg);height:42px;display:flex;align-items:center;padding:0 14px;gap:0;font-size:8.5px;color:var(--ink);margin-top:auto}
  .legend-item{display:flex;align-items:center;gap:7px}
  .legend-item + .legend-item{margin-left:auto;margin-right:26px}
  .legend-dot{width:12px;height:12px;border:1px solid var(--brand-teal);border-radius:50%;background:var(--white)}
  .daily-goal{background:var(--brand-blue);color:var(--white);height:44px;flex:none;display:flex;align-items:center;justify-content:center;font-weight:800;font-size:17px;letter-spacing:.3px}
</style>
</head>
<body>

<svg class="sprite" aria-hidden="true">
  <symbol id="i-menu" viewBox="0 0 24 24"><path d="M3 6h18M3 12h18M3 18h18" stroke="currentColor" stroke-width="1.6" fill="none"/></symbol>
  <symbol id="i-bell" viewBox="0 0 24 24"><path d="M6 17V11a6 6 0 0 1 12 0v6l1.5 2h-15zM10 21h4M12 3v2" stroke="currentColor" stroke-width="1.5" fill="none" stroke-linejoin="round"/></symbol>
  <symbol id="i-gear" viewBox="0 0 24 24"><circle cx="12" cy="12" r="3.2" stroke="currentColor" stroke-width="1.5" fill="none"/><path d="M12 2.5l2 2.3 3-.6.8 3 2.8 1.3-1 2.9 1 2.9-2.8 1.3-.8 3-3-.6-2 2.3-2-2.3-3 .6-.8-3-2.8-1.3 1-2.9-1-2.9 2.8-1.3.8-3 3 .6z" stroke="currentColor" stroke-width="1.4" fill="none" stroke-linejoin="round"/></symbol>
  <symbol id="i-user" viewBox="0 0 24 24"><circle cx="12" cy="7" r="5" fill="currentColor"/><path d="M2 23c0-6 4.5-9 10-9s10 3 10 9z" fill="currentColor"/></symbol>
  <symbol id="i-bars" viewBox="0 0 24 24"><rect x="3" y="11" width="5" height="11" fill="currentColor"/><rect x="10" y="4" width="5" height="18" fill="currentColor"/><rect x="17" y="8" width="5" height="14" fill="currentColor"/></symbol>
  <symbol id="i-add" viewBox="0 0 24 24"><circle cx="12" cy="12" r="10" stroke="currentColor" stroke-width="1.6" fill="none"/><path d="M12 7v10M7 12h10" stroke="currentColor" stroke-width="1.6"/></symbol>
  <symbol id="i-doc" viewBox="0 0 24 24"><path d="M5 2h10l5 5v15H5z M15 2v5h5" stroke="currentColor" stroke-width="1.5" fill="none" stroke-linejoin="round"/><path d="M8 11h9M8 14h9M8 17h9" stroke="currentColor" stroke-width="1.3"/></symbol>
  <symbol id="i-search" viewBox="0 0 24 24"><circle cx="10" cy="10" r="7" stroke="currentColor" stroke-width="1.8" fill="none"/><path d="M15 15l7 7" stroke="currentColor" stroke-width="1.8"/></symbol>
  <symbol id="i-back" viewBox="0 0 24 24"><path d="M18 3L5 12l13 9z" stroke="currentColor" stroke-width="1.8" fill="none" stroke-linejoin="round"/></symbol>
  <symbol id="i-home" viewBox="0 0 24 24"><circle cx="12" cy="12" r="9" stroke="currentColor" stroke-width="1.8" fill="none"/></symbol>
  <symbol id="i-recent" viewBox="0 0 24 24"><rect x="3" y="3" width="18" height="18" stroke="currentColor" stroke-width="1.8" fill="none"/></symbol>

  <symbol id="gauge-art" viewBox="0 0 550 822">
    <rect width="550" height="822" fill="#ffffff"/>
    <path d="M0 0H550V324Q275 160 0 324Z" fill="#20b29b"/>
    <g fill="#ffffff" text-anchor="middle" font-family="Outfit, sans-serif">
      <text x="275" y="60" font-size="27" font-weight="700">SUGAR COUNT</text>
      <text x="275" y="128" font-size="56" font-weight="800">10</text>
      <text x="275" y="172" font-size="23" font-weight="700" letter-spacing="6">SUGAR TODAY</text>
      <text x="275" y="206" font-size="17" font-weight="700">GOAL</text>
    </g>
    <path id="consumption-arc" d="M-10 450Q280 205 570 460" fill="none"/>
    <text font-family="Outfit, sans-serif" font-size="38" font-weight="800" fill="#228bc8" letter-spacing="1">
      <textPath href="#consumption-arc" startOffset="50%" text-anchor="middle">CONSUMPTION TODAY</textPath>
    </text>
    <circle cx="275" cy="800" r="364" fill="none" stroke="#228bc8" stroke-width="60"/>
    <g fill="#ffffff" font-family="Outfit, sans-serif" font-size="26" text-anchor="middle">
      <text x="52" y="522">1</text>
      <text x="141" y="470">2</text>
      <text x="275" y="442">3</text>
      <text x="420" y="474">4</text>
      <text x="510" y="530">5</text>
    </g>
    <g fill="#228bc8" font-family="Outfit, sans-serif" font-size="17" text-anchor="middle">
      <text x="273" y="492">Fatal</text>
      <text x="110" y="562">Danger</text>
      <text x="412" y="567">Catastrophe</text>
    </g>
  </symbol>
</svg>

<!-- Home dashboard, phone size -->
<section class="screen screen--phone" aria-label="Home dashboard, phone">
  <header class="app-bar">
    <svg class="icon"><use href="#i-menu"/></svg>
    <div class="brand"><div class="brand-name">GLYPATH</div><div class="brand-sub">Diabetes restore</div></div>
    <div class="app-bar-actions"><svg class="icon"><use href="#i-bell"/></svg><svg class="icon"><use href="#i-gear"/></svg></div>
  </header>
  <svg class="gauge" preserveAspectRatio="xMidYMin meet" viewBox="0 0 550 822" role="img" aria-label="Sugar count gauge"><use href="#gauge-art"/></svg>
  <nav class="tab-bar">
    <svg class="icon"><use href="#i-user"/></svg><svg class="icon"><use href="#i-bars"/></svg><svg class="icon"><use href="#i-add"/></svg><svg class="icon"><use href="#i-doc"/></svg><svg class="icon"><use href="#i-search"/></svg>
  </nav>
  <div class="system-bar">
    <svg class="icon"><use href="#i-back"/></svg><svg class="icon"><use href="#i-home"/></svg><svg class="icon"><use href="#i-recent"/></svg>
  </div>
</section>

<!-- Home dashboard -->
<section class="screen screen--home" aria-label="Home dashboard">
  <header class="app-bar">
    <svg class="icon"><use href="#i-menu"/></svg>
    <div class="brand"><div class="brand-name">GLYPATH</div><div class="brand-sub">Diabetes restore</div></div>
    <div class="app-bar-actions"><svg class="icon"><use href="#i-bell"/></svg><svg class="icon"><use href="#i-gear"/></svg></div>
  </header>
  <svg class="gauge" preserveAspectRatio="xMidYMin meet" viewBox="0 0 550 822" role="img" aria-label="Sugar count gauge"><use href="#gauge-art"/></svg>
  <nav class="tab-bar">
    <svg class="icon"><use href="#i-user"/></svg><svg class="icon"><use href="#i-bars"/></svg><svg class="icon"><use href="#i-add"/></svg><svg class="icon"><use href="#i-doc"/></svg><svg class="icon"><use href="#i-search"/></svg>
  </nav>
</section>

<!-- Daily feed -->
<section class="screen screen--feed" aria-label="Daily feed">
  <header class="app-bar">
    <svg class="icon"><use href="#i-menu"/></svg>
    <div class="brand"><div class="brand-name">GLYPATH</div><div class="brand-sub">Diabetes restore</div></div>
    <div class="app-bar-actions"><svg class="icon"><use href="#i-bell"/></svg><svg class="icon"><use href="#i-gear"/></svg></div>
  </header>
  <div class="section-title">DAILY FEED</div>
  <form class="feed-form">
    <label class="field-label">Fasting Sugar</label>
    <span class="field-input"></span>
    <label class="field-label">Random Sugar</label>
    <span class="field-input"></span>
    <label class="field-label">Daily Walk Time / Distance</label>
    <span class="field-input"></span>
    <span class="submit">SUBMIT</span>
  </form>
  <nav class="tab-bar">
    <svg class="icon"><use href="#i-user"/></svg><svg class="icon"><use href="#i-bars"/></svg><svg class="icon"><use href="#i-add"/></svg><svg class="icon"><use href="#i-doc"/></svg><svg class="icon"><use href="#i-search"/></svg>
  </nav>
</section>

<!-- Rehab monitor -->
<section class="screen screen--rehab" aria-label="Rehab monitor">
  <header class="app-bar">
    <svg class="icon"><use href="#i-menu"/></svg>
    <div class="brand"><div class="brand-name">GLYPATH</div><div class="brand-sub">Diabetes restore</div></div>
    <div class="app-bar-actions"><svg class="icon"><use href="#i-bell"/></svg><svg class="icon"><use href="#i-gear"/></svg></div>
  </header>
  <div class="section-title">REHAB MONITOR</div>
  <div class="rehab-body">
    <svg class="chart" viewBox="0 0 550 265" height="127" role="img" aria-label="Daily sugar area chart">
      <g stroke="#cfcfcf" stroke-dasharray="3 3" stroke-width="1">
        <path d="M73 20H528M73 58H528M73 96H528M73 134H528M73 172H528M73 210H528M73 248H528"/>
        <path d="M73 20V255M150 20V255M226 20V255M302 20V255M378 20V255M454 20V255M528 20V255"/>
      </g>
      <g font-family="Outfit, sans-serif" font-size="16" fill="#555" text-anchor="end">
        <text x="50" y="28">300</text><text x="50" y="66">250</text><text x="50" y="104">200</text>
        <text x="50" y="142">150</text><text x="50" y="180">100</text><text x="50" y="218">50</text><text x="50" y="258">0</text>
      </g>
      <path d="M73 96L140 58L202 138L282 62L338 136L400 84L480 130L528 97V255H73Z" fill="var(--chart-blue)"/>
    </svg>
    <div class="chart-caption chart-caption--sugar">Daily Sugar Graph</div>
    <svg class="chart" viewBox="0 0 550 278" height="136" role="img" aria-label="Daily walk and exercise bar chart">
      <g stroke="#9a9a9a" stroke-dasharray="2 3" stroke-width="1">
        <path d="M48 13H530M48 37H530M48 62H530M48 86H530M48 111H530M48 135H530M48 160H530M48 184H530M48 209H530M48 233H530M48 257H530"/>
      </g>
      <g>
        <rect x="20" y="6" width="17" height="13" fill="var(--bar-lime)"/>
        <rect x="20" y="31" width="17" height="13" fill="var(--bar-aqua)"/>
        <rect x="20" y="55" width="17" height="13" fill="var(--bar-navy)"/>
        <rect x="20" y="80" width="17" height="13" fill="var(--bar-coral)"/>
        <rect x="20" y="104" width="17" height="13" fill="var(--bar-amber)"/>
        <rect x="20" y="129" width="17" height="13" fill="var(--bar-violet)"/>
        <rect x="20" y="153" width="17" height="13" fill="var(--bar-jade)"/>
      </g>
      <g font-family="Outfit, sans-serif" font-size="10" text-anchor="middle">
        <g fill="#ffffff">
          <text x="28.5" y="16">20</text><text x="28.5" y="41">18</text><text x="28.5" y="65">16</text>
          <text x="28.5" y="90">14</text><text x="28.5" y="114">12</text><text x="28.5" y="139">10</text><text x="28.5" y="163">8</text>
        </g>
        <g fill="#444">
          <text x="28.5" y="188">6</text><text x="28.5" y="212">4</text><text x="28.5" y="237">2</text><text x="28.5" y="261">0</text>
        </g>
      </g>
      <g>
        <rect x="65" y="105" width="44" height="152" fill="var(--bar-lime)"/>
        <rect x="127" y="146" width="44" height="111" fill="var(--bar-aqua)"/>
        <rect x="194" y="43" width="44" height="214" fill="var(--bar-navy)"/>
        <rect x="259" y="88" width="44" height="169" fill="var(--bar-coral)"/>
        <rect x="324" y="16" width="44" height="241" fill="var(--bar-amber)"/>
        <rect x="388" y="121" width="44" height="136" fill="var(--bar-violet)"/>
        <rect x="453" y="88" width="44" height="169" fill="var(--bar-jade)"/>
      </g>
      <g font-family="Outfit, sans-serif" font-size="9" fill="#444" text-anchor="middle">
        <text x="87" y="272">1/16</text><text x="149" y="272">2/16</text><text x="216" y="272">3/16</text>
        <text x="281" y="272">4/16</text><text x="346" y="272">5/16</text><text x="410" y="272">6/16</text><text x="475" y="272">7/16</text>
      </g>
    </svg>
    <div class="chart-caption chart-caption--walk">Daily Walk/Exercise</div>
    <div class="legend">
      <span class="legend-item"><span class="legend-dot"></span>Sugar Bite Sent Weekly</span>
      <span class="legend-item"><span class="legend-dot"></span>Weekly Avg</span>
    </div>
  </div>
  <div class="daily-goal">DAILY GOAL</div>
  <nav class="tab-bar">
    <svg class="icon"><use href="#i-user"/></svg><svg class="icon"><use href="#i-bars"/></svg><svg class="icon"><use href="#i-add"/></svg><svg class="icon"><use href="#i-doc"/></svg><svg class="icon"><use href="#i-search"/></svg>
  </nav>
</section>

</body>
</html>
```